Brochure Design Project

This will be a tri-fold full 8.5x11 brochure that will be distributed and sitting in Oncology offices all throughout the US. It is a lead generation and referral designed piece that it to target all patients, Cancer primarily, but all critically ill patients and seniors above the age of 70. We want our service to go beyond just a financial transaction, we want to educate patients of their rights within a life insurance policy and if we cannot help them personally, do want to assist them by referring them to other agencies and non profits than can. ( I want to redesign the brochure attached, it can be very similar and need only minor changes to content, but would welcome all suggestions on improving message, and in gaining attention, picture substitutions and change of colors, along with the layout itself can be improved upon, and I need this piece to look very professional and appropriate for medical offices. I will be needing assistance on several upcoming projects and will also have great printing demands.

Target Market(s)

Cancer patients
all chronically and critically ill patients
all seniors above age 70

Industry/Entity Type

Life Insurance

Requirements
Must have
• Cancer and the terminally ill
Nice to have
• seniors above 70

```html
<!DOCTYPE html>
<html lang="en">
<head>
<meta charset="utf-8">
<title>Beacon Settlements – Tri-fold Brochure</title>
<link href="https://fonts.googleapis.com/css2?family=Questrial&family=Montserrat:wght@400;600;700&display=swap" rel="stylesheet">
<style>
  :root {
    --orange: #f5a91c;
    --orange-deep: #e8980c;
    --blue: #4a7dc6;
    --blue-deep: #2f5fae;
    --ink: #1c1c1c;
    --paper: #ffffff;
    --backdrop: #c9cbc4;
  }
  * { box-sizing: border-box; margin: 0; padding: 0; }
  html, body { width: 1200px; height: 1200px; overflow: hidden; }
  body {
    background: var(--backdrop);
    font-family: "Questrial", "Century Gothic", sans-serif;
    color: var(--ink);
    position: relative;
  }
  .brochure {
    position: absolute; left: 45px; top: 171px;
    width: 1110px; height: 858px;
    display: flex;
    box-shadow: 0 10px 30px rgba(0,0,0,.25);
  }
  .panel { position: relative; width: 370px; height: 100%; overflow: hidden; background: var(--paper); }
  .panel + .panel { border-left: 1px solid rgba(0,0,0,.08); }

  /* brand name */
  .brand { display: flex; align-items: center; gap: 12px; justify-content: center; }
  .brand-dot { width: 22px; height: 22px; border-radius: 50%; background: var(--orange); }
  .brand-name {
    font-family: "Montserrat", sans-serif; font-weight: 600;
    color: var(--blue-deep); font-size: 30px; letter-spacing: 2px; text-align: center; line-height: 1.1;
  }

  /* ---------- Mailer panel ---------- */
  .mailer .brand { position: absolute; top: 70px; left: 0; right: 0; }
  .contact-band {
    position: absolute; top: 205px; left: 0; right: 0; height: 150px;
    background: var(--orange); text-align: center; padding-top: 20px;
  }
  .contact-band .note { font-size: 15px; line-height: 1.2; }
  .contact-band .phone { font-family: "Montserrat", sans-serif; font-weight: 600; font-size: 34px; margin: 6px 0 4px; }
  .contact-band .confidential { font-size: 16px; line-height: 1.2; }

  .reply-card {
    position: absolute; left: -74px; top: 414px; width: 518px; height: 370px;
    transform: rotate(90deg);
  }
  .postal-lines { position: absolute; top: 26px; left: 24px; font-size: 9px; font-family: "Montserrat", sans-serif; line-height: 1.5; }
  .postal-lines span { margin-right: 28px; }
  .reply-label {
    position: absolute; top: 62px; left: 24px; width: 290px; height: 36px;
    background: var(--blue); color: #fff; font-family: "Montserrat", sans-serif; font-weight: 700;
    font-size: 20px; line-height: 36px; padding-left: 12px;
  }
  .address { position: absolute; top: 130px; left: 24px; line-height: 1.35; }
  .address .to { font-family: "Montserrat", sans-serif; font-weight: 700; color: var(--blue); font-size: 16px; }
  .address p { font-size: 17px; }
  .facing-marks { position: absolute; top: 22px; left: 340px; display: flex; gap: 6px; }
  .facing-marks i { display: block; width: 5px; height: 56px; background: var(--orange); }
  .indicia {
    position: absolute; top: 18px; right: 18px; width: 96px; height: 108px;
    border: 2px solid var(--blue); outline: 1px solid var(--blue); outline-offset: 3px;
    font-size: 9px; font-family: "Montserrat", sans-serif; color: var(--blue-deep);
    text-align: center; padding-top: 16px; line-height: 1.35;
  }
  .reply-bars { position: absolute; right: 18px; top: 170px; width: 104px; display: flex; flex-direction: column; gap: 7px; }
  .reply-bars i { display: block; height: 6px; background: var(--orange); }

  /* ---------- Inside flap panel ---------- */
  .services { background: var(--blue); }
  .photo { display: block; width: 100%; }
  .services .photo { height: 225px; background: linear-gradient(160deg, #d7d4c6 0%, #b9c3c6 45%, #8b9aa5 100%); }
  .callout {
    position: absolute; top: 250px; left: 30px; right: 30px; height: 140px;
    background: var(--orange); text-align: center; padding-top: 16px;
    box-shadow: 4px 6px 10px rgba(0,0,0,.3);
  }
  .callout .lead { color: var(--blue-deep); font-family: "Montserrat", sans-serif; font-weight: 600; font-size: 20px; }
  .callout .body { font-size: 21px; line-height: 1.15; }
  .callout .action { color: #fff; font-family: "Montserrat", sans-serif; font-weight: 600; font-size: 19px; margin-top: 2px; }
  .benefits { position: absolute; top: 418px; left: 42px; right: 30px; }
  .benefits h2 { color: var(--orange); font-family: "Montserrat", sans-serif; font-weight: 600; font-size: 16px; margin-bottom: 8px; }
  .benefits ul { list-style: none; }
  .benefits li { color: #fff; font-size: 12.5px; line-height: 1.4; display: flex; gap: 6px; }
  .benefits li svg { flex: none; margin-top: 4px; }
  .gift { position: absolute; bottom: 34px; left: 0; right: 0; text-align: center; font-family: "Montserrat", sans-serif; font-size: 15px; line-height: 1.2; }

  /* ---------- Cover panel ---------- */
  .cover .brand { position: absolute; top: 70px; left: 0; right: 0; }
  .tagline { position: absolute; top: 150px; left: 0; right: 0; text-align: center; color: var(--blue-deep); font-size: 22px; line-height: 1.2; }
  .not-alone { position: absolute; top: 225px; left: 0; right: 0; text-align: center; }
  .not-alone h2 { color: var(--orange); font-family: "Montserrat", sans-serif; font-weight: 600; font-size: 24px; }
  .not-alone p { font-size: 19px; line-height: 1.25; margin-top: 4px; }
  .cover .photo { position: absolute; top: 350px; height: 320px; background: linear-gradient(150deg, #e4dccd 0%, #c9b7a3 40%, #9fb4c8 100%); }
  .cta-band {
    position: absolute; top: 670px; left: 0; right: 0; bottom: 0;
    background: var(--orange); text-align: center; padding-top: 50px;
  }
  .cta-band .phone { color: #fff; font-family: "Montserrat", sans-serif; font-weight: 600; font-size: 36px; }
  .cta-band .waiting { font-size: 18px; margin-top: 4px; }
</style>
</head>
<body>
<main class="brochure">

  <section class="panel mailer">
    <div class="brand"><span class="brand-dot"></span><span class="brand-name">BEACON<br>Settlements</span></div>
    <div class="contact-band">
      <p class="note">please returen the attahed postcard or<br>call tool free</p>
      <p class="phone">800-555-0147</p>
      <p class="confidential">all communication will<br>be kept strictly confidential!</p>
    </div>
    <div class="reply-card">
      <div class="postal-lines"><span>FIRST CLASS MAIL</span><span>PERMIT NO. 412</span><span>GEORGIA</span><br>POSTAGE WILL BE PAID BY ADDRESSEE</div>
      <div class="reply-label">BUSSINES REPLY MAIL</div>
      <div class="address">
        <p class="to">BEACON SETTLEMENTS</p>
        <p>418 Maple Grove Rd. Brookfield</p>
        <p>Georgia 30099</p>
      </div>
      <div class="facing-marks"><i></i><i></i><i></i><i></i><i></i></div>
      <div class="indicia">NO POSTAGE<br>NECESSARY<br>IF MAILED<br>IN THE<br>UNITED STATES</div>
      <div class="reply-bars"><i></i><i></i><i></i><i></i><i></i><i></i><i></i><i></i><i></i><i></i><i></i><i></i><i></i><i></i></div>
    </div>
  </section>

  <section class="panel services">
    <div class="photo" role="img" aria-label="Photo of seniors seated in a bright hospital waiting room"></div>
    <div class="callout">
      <p class="lead">Don't wait any longer</p>
      <p class="body">we are standing<br>by to help</p>
      <p class="action">contact us now</p>
    </div>
    <div class="benefits">
      <h2>BEACON SETTLEMENTS</h2>
      <ul>
        <li><svg width="10" height="9" viewBox="0 0 10 9"><path d="M1 5l3 3 5-7" fill="none" stroke="#fff" stroke-width="1.8"/></svg>Reduce finincal strees</li>
        <li><svg width="10" height="9" viewBox="0 0 10 9"><path d="M1 5l3 3 5-7" fill="none" stroke="#fff" stroke-width="1.8"/></svg>pay for uninsured Health cost</li>
        <li><svg width="10" height="9" viewBox="0 0 10 9"><path d="M1 5l3 3 5-7" fill="none" stroke="#fff" stroke-width="1.8"/></svg>pay for Alternetive Treatment</li>
        <li><svg width="10" height="9" viewBox="0 0 10 9"><path d="M1 5l3 3 5-7" fill="none" stroke="#fff" stroke-width="1.8"/></svg>improve quality of life</li>
        <li><svg width="10" height="9" viewBox="0 0 10 9"><path d="M1 5l3 3 5-7" fill="none" stroke="#fff" stroke-width="1.8"/></svg>pay off debt</li>
        <li><svg width="10" height="9" viewBox="0 0 10 9"><path d="M1 5l3 3 5-7" fill="none" stroke="#fff" stroke-width="1.8"/></svg>take along Awaited Vacation or Dream trip</li>
        <li><svg width="10" height="9" viewBox="0 0 10 9"><path d="M1 5l3 3 5-7" fill="none" stroke="#fff" stroke-width="1.8"/></svg>Make cash gifts to family and friends</li>
        <li><svg width="10" height="9" viewBox="0 0 10 9"><path d="M1 5l3 3 5-7" fill="none" stroke="#fff" stroke-width="1.8"/></svg>fulfill life wishs</li>
        <li><svg width="10" height="9" viewBox="0 0 10 9"><path d="M1 5l3 3 5-7" fill="none" stroke="#fff" stroke-width="1.8"/></svg>pay for college funding</li>
        <li><svg width="10" height="9" viewBox="0 0 10 9"><path d="M1 5l3 3 5-7" fill="none" stroke="#fff" stroke-width="1.8"/></svg>Make home improvements</li>
        <li><svg width="10" height="9" viewBox="0 0 10 9"><path d="M1 5l3 3 5-7" fill="none" stroke="#fff" stroke-width="1.8"/></svg>Donate to church charity</li>
        <li><svg width="10" height="9" viewBox="0 0 10 9"><path d="M1 5l3 3 5-7" fill="none" stroke="#fff" stroke-width="1.8"/></svg>see the money enjoyed by relative now</li>
        <li><svg width="10" height="9" viewBox="0 0 10 9"><path d="M1 5l3 3 5-7" fill="none" stroke="#fff" stroke-width="1.8"/></svg>Invest in fnianacal Vehicles</li>
        <li><svg width="10" height="9" viewBox="0 0 10 9"><path d="M1 5l3 3 5-7" fill="none" stroke="#fff" stroke-width="1.8"/></svg>Buy a new car</li>
        <li><svg width="10" height="9" viewBox="0 0 10 9"><path d="M1 5l3 3 5-7" fill="none" stroke="#fff" stroke-width="1.8"/></svg>Fund long term care expenses</li>
        <li><svg width="10" height="9" viewBox="0 0 10 9"><path d="M1 5l3 3 5-7" fill="none" stroke="#fff" stroke-width="1.8"/></svg>Plan Ahead for final Estate needs</li>
      </ul>
    </div>
    <p class="gift">BEACON IS OUR<br>DESIRED GIFT TO YOU</p>
  </section>

  <section class="panel cover">
    <div class="brand"><span class="brand-dot"></span><span class="brand-name">BEACON<br>Settlements</span></div>
    <p class="tagline">DISCOVER<br>FINANCIAL FREEDOM</p>
    <div class="not-alone">
      <h2>YOUR NOT ALONE</h2>
      <p>Finacial Resources are<br>Available!</p>
    </div>
    <div class="photo" role="img" aria-label="Photo of a family visiting a grandparent in a hospital room"></div>
    <div class="cta-band">
      <p class="phone">800-555-0147</p>
      <p class="waiting">We are waiting to help!</p>
    </div>
  </section>

</main>
</body>
</html>
```